New stationery design project

Until now, Brolin Technology was exclusively geared towards marketing the self-warming toasty-step insole. Corresponding designer material exists for this purpose, which is further used in this line of business. In the meantime, the business purpose has been expanded to include the following activities: "The company provides consulting services and takes on board mandates in the field of energy and information technology as well as personality-enhancing coaching." We now need a suitable stationery design (letterhead, business card) for this new business purpose. The design is intended to convey specialist knowledge and many years of experience

```html
<!DOCTYPE html>
<html lang="en">
<head>
<meta charset="utf-8">
<title>Brolin Technology – Stationery</title>
<link href="https://fonts.googleapis.com/css2?family=Poppins:wght@400;600;700&family=Open+Sans:wght@400&display=swap" rel="stylesheet">
<style>
  :root {
    --backdrop: #e5e5e5;
    --paper: #f1f1f1;
    --ink: #3c3c3c;
    --ink-soft: #555555;
    --brand-blue: #2a8ccc;
    --brand-dark: #3a3a3a;
    --fold-line: #dcdcdc;
    --shadow: rgba(0,0,0,0.13);
  }
  * { box-sizing: border-box; margin: 0; padding: 0; }
  html, body { width: 1200px; height: 795px; overflow: hidden; }
  body {
    background: var(--backdrop);
    font-family: "Poppins", sans-serif;
    color: var(--ink);
    position: relative;
  }
  .sheet {
    position: absolute;
    background: var(--paper);
    box-shadow: 0 2px 6px var(--shadow);
    overflow: hidden;
  }
  .brand {
    display: flex;
    align-items: center;
    gap: 0.35em;
    font-family: "Poppins", sans-serif;
    font-weight: 700;
    color: var(--brand-dark);
    letter-spacing: 0.03em;
    white-space: nowrap;
    line-height: 1;
  }
  .brand-square {
    width: 0.6em; height: 0.6em;
    background: var(--brand-blue);
    flex: none;
  }
  .contact-line { display: flex; align-items: center; gap: 2px; white-space: nowrap; }
  .contact-line svg { flex: none; }

  /* Letterhead */
  .letterhead { left: 293px; top: 99px; width: 292px; height: 415px; }
  .letterhead .brand { position: absolute; top: 30px; left: 0; right: 0; justify-content: center; font-size: 9px; }
  .letter-body {
    position: absolute; left: 26px; top: 92px; width: 240px;
    font-family: "Open Sans", sans-serif;
    font-size: 5.3px; line-height: 8px; color: var(--ink-soft);
    text-align: justify;
  }
  .letter-body p { margin-bottom: 8px; }
  .signature {
    width: 36px; height: 32px; margin-top: 4px;
    background: linear-gradient(135deg, #e6e6e6, #dcdcdc);
  }
  .letter-footer {
    position: absolute; left: 26px; right: 26px; top: 371px;
    display: flex; justify-content: space-between;
    font-size: 5.6px; line-height: 7.4px; color: var(--ink);
  }
  .letter-footer .contact-line svg { width: 5px; height: 5px; }
  .sender { text-align: right; white-space: nowrap; }
  .sender .company { color: var(--brand-blue); }

  /* Folder */
  .folder { left: 637px; top: 80px; width: 346px; height: 437px; }
  .folder-spine { position: absolute; top: 0; bottom: 0; width: 1px; background: var(--fold-line); }
  .folder .brand { position: absolute; left: 20px; right: 0; top: 210px; justify-content: center; font-size: 18px; }
  .folder-url {
    position: absolute; left: 20px; right: 0; top: 398px;
    text-align: center; font-size: 9px; font-weight: 600; color: var(--brand-dark);
  }
  .folder-url span { color: var(--brand-blue); }

  /* Business cards */
  .card { left: 187px; width: 132px; height: 75px; }
  .card-front { top: 551px; }
  .card-front .brand { position: absolute; left: 0; right: 0; top: 34px; justify-content: center; font-size: 7px; }
  .card-back { top: 646px; }
  .card-back .brand { position: absolute; right: 11px; top: 15px; font-size: 5px; }
  .card-person { position: absolute; left: 11px; right: 11px; top: 41px; border-bottom: 0.6px solid var(--brand-blue); padding-bottom: 1px; }
  .card-person .name { font-size: 4.3px; font-weight: 600; line-height: 5px; }
  .card-person .role { font-size: 3px; color: var(--brand-blue); line-height: 4px; }
  .card-details {
    position: absolute; left: 11px; right: 11px; top: 52px;
    display: flex; justify-content: space-between;
    font-size: 2.8px; line-height: 4.2px;
  }
  .card-details .contact-line svg { width: 3px; height: 3px; }
  .card-details .sender .company { color: var(--ink); }

  /* Envelopes */
  .envelope { top: 561px; width: 329px; height: 157px; }
  .envelope-front { left: 353px; }
  .envelope-front .brand { position: absolute; left: 22px; top: 32px; font-size: 7px; }
  .envelope-address { position: absolute; left: 22px; top: 45px; font-size: 6px; line-height: 8.4px; color: var(--ink); padding-left: 12px; }
  .envelope-back { left: 713px; }
  .envelope-back svg.flap { position: absolute; left: 0; top: 0; }
  .envelope-back .brand { position: absolute; left: 0; right: 0; top: 20px; justify-content: center; font-size: 6px; }
</style>
</head>
<body>

  <section class="sheet letterhead" aria-label="Letterhead">
    <div class="brand"><span class="brand-square"></span>BROLIN TECHNOLOGY</div>
    <div class="letter-body">
      <p>Dear customer,</p>
      <p>Lorem ipsum dolor sit amet, consectetur adipisicing elit, sed do eiusmod tempor incididunt ut labore et dolore magna aliqua. Ut enim ad minim veniam, quis nostrud exercitation ullamco laboris nisi ut aliquip ex ea commodo consequat. Duis aute irure dolor in reprehenderit in voluptate velit esse cillum dolore eu fugiat nulla pariatur. Excepteur sint occaecat cupidatat non proident, sunt in culpa qui officia deserunt mollit anim id est laborum.</p>
      <p>Lorem ipsum dolor sit amet, consectetur adipisicing elit, sed do eiusmod tempor incididunt ut labore et dolore magna aliqua. Ut enim ad minim veniam, quis nostrud exercitation ullamco laboris nisi ut aliquip ex ea commodo consequat. Duis aute irure dolor in reprehenderit in voluptate velit esse cillum dolore eu fugiat nulla pariatur. Excepteur sint occaecat cupidatat non proident, sunt in culpa qui officia deserunt mollit anim id est laborum.</p>
      <p>Lorem ipsum dolor sit amet, consectetur adipisicing elit, sed do eiusmod tempor incididunt ut labore et dolore magna aliqua. Ut enim ad minim veniam, quis nostrud exercitation ullamco laboris nisi ut aliquip ex ea commodo consequat. Duis aute irure dolor in reprehenderit in voluptate velit esse cillum dolore eu fugiat nulla pariatur. Excepteur sint occaecat cupidatat non proident, sunt in culpa qui officia deserunt mollit anim id est laborum.</p>
      <p>Lorem ipsum dolor sit amet, consectetur adipisicing elit, sed do eiusmod tempor incididunt ut labore et dolore magna aliqua. Ut enim ad minim veniam, quis nostrud exercitation ullamco laboris nisi ut aliquip ex ea commodo consequat. Duis aute irure dolor in reprehenderit.</p>
      <p>Yours Sincerely,</p>
      <div class="signature" role="img" aria-label="Handwritten signature"></div>
    </div>
    <div class="letter-footer">
      <div class="contacts">
        <div class="contact-line"><svg viewBox="0 0 10 10"><path d="M2 1 L4 1 L4.6 3.4 L3.4 4.2 Q4.4 6 6 6.8 L6.8 5.6 L9 6.2 L9 8.4 Q5 9 1.8 5.4 Q1 3 2 1Z" fill="#2a8ccc"/></svg>+41 79 512 08 64</div>
        <div class="contact-line"><svg viewBox="0 0 10 10"><rect x="0.5" y="2" width="9" height="6.5" fill="#2a8ccc"/><path d="M0.5 2 L5 5.5 L9.5 2" stroke="#fff" stroke-width="0.8" fill="none"/></svg>marcel.ostertag@brolin-technology.ch</div>
        <div class="contact-line"><svg viewBox="0 0 10 10"><circle cx="5" cy="5" r="4.2" stroke="#2a8ccc" fill="none"/><path d="M0.8 5 H9.2 M5 0.8 Q2.5 5 5 9.2 Q7.5 5 5 0.8" stroke="#2a8ccc" fill="none" stroke-width="0.7"/></svg>www.brolin-technology.ch</div>
      </div>
      <div class="sender">
        <div class="company">Brolin Technology GmbH</div>
        <div>Lindenweg 14</div>
        <div>CH - 8604 Talwil</div>
      </div>
    </div>
  </section>

  <section class="sheet folder" aria-label="Presentation folder">
    <span class="folder-spine" style="left:7px"></span>
    <span class="folder-spine" style="left:13px"></span>
    <span class="folder-spine" style="left:19px"></span>
    <div class="brand"><span class="brand-square"></span>BROLIN TECHNOLOGY</div>
    <div class="folder-url">www.<span>brolin-technology</span>.ch</div>
  </section>

  <section class="sheet card card-front" aria-label="Business card front">
    <div class="brand"><span class="brand-square"></span>BROLIN TECHNOLOGY</div>
  </section>

  <section class="sheet card card-back" aria-label="Business card back">
    <div class="brand"><span class="brand-square"></span>BROLIN TECHNOLOGY</div>
    <div class="card-person">
      <div class="name">MARCEL OSTERTAG</div>
      <div class="role">Geschäftsinhaber</div>
    </div>
    <div class="card-details">
      <div>
        <div class="contact-line"><svg viewBox="0 0 10 10"><path d="M2 1 L4 1 L4.6 3.4 L3.4 4.2 Q4.4 6 6 6.8 L6.8 5.6 L9 6.2 L9 8.4 Q5 9 1.8 5.4 Q1 3 2 1Z" fill="#2a8ccc"/></svg>+41 79 512 08 64</div>
        <div class="contact-line"><svg viewBox="0 0 10 10"><rect x="0.5" y="2" width="9" height="6.5" fill="#2a8ccc"/></svg>marcel.ostertag@brolin-technology.ch</div>
        <div class="contact-line"><svg viewBox="0 0 10 10"><circle cx="5" cy="5" r="4.2" stroke="#2a8ccc" fill="none"/></svg>www.brolin-technology.ch</div>
      </div>
      <div class="sender">
        <div class="company">Brolin Technology GmbH</div>
        <div>Lindenweg 14</div>
        <div>CH - 8604 Talwil</div>
      </div>
    </div>
  </section>

  <section class="sheet envelope envelope-front" aria-label="Envelope front">
    <div class="brand"><span class="brand-square"></span>BROLIN TECHNOLOGY</div>
    <div class="envelope-address">
      <div>Lindenweg 14</div>
      <div>CH - 8604 Talwil</div>
    </div>
  </section>

  <section class="sheet envelope envelope-back" aria-label="Envelope back">
    <svg class="flap" width="329" height="157" viewBox="0 0 329 157">
      <path d="M1 2 L7 52 Q8 56 13 56 L316 56 Q321 56 322 52 L328 2" fill="none" stroke="#dedede" stroke-width="0.8"/>
    </svg>
    <div class="brand"><span class="brand-square"></span>BROLIN TECHNOLOGY</div>
  </section>

</body>
</html>
```